Business Cards for Law Office of Miriam T. Haskell

I need a business card for my new estate planning law firm. I have attached my logo. I would like a design that is professional but not too formal or stuffy.

Target Market(s)

Professionals (lawyers, doctors, businesswomen) between the age of 30 and 50 who are tech-savvy and educated.

Industry/Entity Type

Lawyer

Contact Information for Business Card

Miriam T. Haskell

582 E. 67th Street
9th Floor
New York, NY 10065

Phone: (855) 407-6218
Direct: (917) 563-0472
Email: Miriam@MiriamTHaskellLaw.example
www.MiriamTHaskellLaw.example

Font styles to use
Other font styles liked:
• Corbel

Requirements
Must have
• On the front:
• Miriam T. Haskell, Esq.
• Owner & Founder
• 582 E. 67th Street
• 9th Floor
• New York, NY 10065
• Phone: (855) 407-6218
• Direct: (917) 563-0472
• Email: miriam@miriamthaskelllaw.example
• www.miriamthaskelllaw.example
• On the back:
• LOGO
Nice to have
• I want it to be professional but not too formal or stuffy. Please choose colors that go with my logo.
Should not have
• I don't want TOO MUCH color. Some color is good, but not too much.

```html
<!DOCTYPE html>
<html lang="en">
<head>
<meta charset="UTF-8">
<title>Business Cards – Law Office of Miriam T. Haskell</title>
<link href="https://fonts.googleapis.com/css2?family=Lato:wght@400;700&display=swap" rel="stylesheet">
<style>
  :root {
    --plum: #7b2a82;
    --plum-deep: #6a2371;
    --orange: #f07f1d;
    --ink: #2b2b2b;
    --paper: #ffffff;
    --backdrop: #e8e6e9;
  }
  * { box-sizing: border-box; margin: 0; padding: 0; }
  html, body { width: 1200px; height: 800px; overflow: hidden; }
  body {
    background: var(--backdrop);
    font-family: "Lato", "Corbel", sans-serif;
    position: relative;
  }
  .card {
    position: absolute;
    width: 540px;
    height: 309px;
    border-radius: 3px;
    overflow: hidden;
    box-shadow: 0 10px 28px rgba(60, 20, 70, 0.22);
  }
  .card-back {
    left: 40px;
    top: 150px;
    background: var(--plum);
    display: flex;
    align-items: center;
    justify-content: center;
  }
  .card-front {
    left: 620px;
    top: 340px;
    background: var(--paper);
  }
  .swoosh { position: absolute; inset: 0; width: 540px; height: 309px; }

  .firm-name { font-weight: 400; line-height: 1; letter-spacing: 0.04em; }
  .firm-name .prefix { display: block; font-size: 12px; letter-spacing: 0.14em; margin-bottom: 5px; }
  .firm-name .main { display: block; font-size: 27px; }
  .card-back .firm-name { color: var(--paper); text-align: center; }
  .card-front .firm-name { position: absolute; left: 36px; top: 48px; color: var(--plum); }
  .card-front .firm-name .main { font-size: 25px; }

  .person { position: absolute; left: 36px; top: 150px; }
  .person-name { font-size: 20px; font-weight: 700; color: var(--plum); }
  .person-role { font-size: 13px; color: var(--ink); margin-top: 2px; }

  .address {
    position: absolute; left: 36px; top: 215px;
    font-size: 14px; line-height: 1.3; color: var(--ink); font-style: normal;
  }

  .contact-list {
    position: absolute; left: 290px; top: 158px;
    list-style: none; font-size: 11.5px; color: var(--ink);
  }
  .contact-list li { display: flex; align-items: center; gap: 8px; height: 20px; }
  .contact-list svg { width: 11px; height: 11px; fill: var(--plum); flex: none; }
</style>
</head>
<body>

  <section class="card card-back" aria-label="Card back">
    <h1 class="firm-name">
      <span class="prefix">LAW OFFICE OF</span>
      <span class="main">MIRIAM T. HASKELL</span>
    </h1>
  </section>

  <section class="card card-front" aria-label="Card front">
    <svg class="swoosh" viewBox="0 0 540 309" aria-hidden="true">
      <path d="M210,0 H540 V132 Q470,22 210,0 Z" fill="var(--plum)"/>
      <path d="M210,0 Q470,22 540,132 V156 Q462,36 210,0 Z" fill="var(--orange)"/>
    </svg>

    <h2 class="firm-name">
      <span class="prefix">LAW OFFICE OF</span>
      <span class="main">MIRIAM T. HASKELL</span>
    </h2>

    <div class="person">
      <p class="person-name">Miriam T. Haskell, Esq.</p>
      <p class="person-role">Owner &amp; Founder</p>
    </div>

    <address class="address">
      582 E. 67th Street<br>
      9th Floor<br>
      New York, NY 10065
    </address>

    <ul class="contact-list">
      <li>
        <svg viewBox="0 0 24 24"><path d="M6.6 10.8a15.1 15.1 0 0 0 6.6 6.6l2.2-2.2a1 1 0 0 1 1-.25 11.4 11.4 0 0 0 3.6.57 1 1 0 0 1 1 1V20a1 1 0 0 1-1 1A17 17 0 0 1 3 4a1 1 0 0 1 1-1h3.5a1 1 0 0 1 1 1c0 1.25.2 2.45.57 3.57a1 1 0 0 1-.25 1z"/></svg>
        (855) 407-6218
      </li>
      <li>
        <svg viewBox="0 0 24 24"><path d="M6.6 10.8a15.1 15.1 0 0 0 6.6 6.6l2.2-2.2a1 1 0 0 1 1-.25 11.4 11.4 0 0 0 3.6.57 1 1 0 0 1 1 1V20a1 1 0 0 1-1 1A17 17 0 0 1 3 4a1 1 0 0 1 1-1h3.5a1 1 0 0 1 1 1c0 1.25.2 2.45.57 3.57a1 1 0 0 1-.25 1z"/></svg>
        (917) 563-0472
      </li>
      <li>
        <svg viewBox="0 0 24 24"><path d="M2 5h20v14H2z M2 5l10 8 10-8" fill="var(--plum)" stroke="#fff" stroke-width="1.5"/></svg>
        miriam@miriamthaskelllaw.example
      </li>
      <li>
        <svg viewBox="0 0 24 24"><circle cx="12" cy="12" r="10"/><path d="M2 12h20M12 2c3 3 3 17 0 20M12 2c-3 3-3 17 0 20" stroke="#fff" stroke-width="1.3" fill="none"/></svg>
        www.miriamthaskelllaw.example
      </li>
    </ul>
  </section>

</body>
</html>
```